use the existing webpage www.lyravelbeauty.ch an create a modern style page using the same logos pictures and text . t
Target Market(s)
healthcare and cosmetigs
Number of Pages Required
1 page
Requirements
Must have
- same cooperate identity and style as the original lyravelbeauty.ch
- a link to the webshop: https://www.lyravelbeauty.webstores.ch/ (no new window)
- ignore evntual text written in polish language.

```html
<!DOCTYPE html>
<html lang="de">
<head>
<meta charset="utf-8">
<title>Lyravel Beauty – The Promise of a Longer Look</title>
<link rel="stylesheet" href="https://fonts.googleapis.com/css2?family=Playfair+Display:wght@400;700&family=Montserrat:wght@400;500;600;700&display=swap">
<style>
:root{
  --navy:#2d2f4b;
  --navy-soft:#3b3e5c;
  --rose:#d99aa3;
  --rose-deep:#c7808b;
  --blush:#f4dcdc;
  --blush-light:#fbf0ef;
  --ink:#3a3a48;
  --muted:#7b7b88;
  --line:#e4d2d2;
  --white:#ffffff;
  --footer:#f3f1f2;
}
*{box-sizing:border-box;margin:0;padding:0}
html,body{width:1200px;height:2724px;overflow:hidden}
body{font-family:"Montserrat",sans-serif;color:var(--ink);background:var(--white);font-size:13px;line-height:1.6;position:relative}
a{color:inherit;text-decoration:none}
.serif{font-family:"Playfair Display",serif}

.topbar{height:40px;background:var(--navy);color:#dcdce6;display:flex;align-items:center;justify-content:space-between;padding:0 60px;font-size:11px}
.topbar .langs{display:flex;gap:8px}
.topbar .langs span{width:14px;height:14px;border-radius:50%;background:var(--rose)}
.topbar .langs span+span{background:#8f91ad}

.header{height:80px;display:flex;align-items:center;justify-content:space-between;padding:0 60px;border-bottom:1px solid var(--line)}
.brand{font-family:"Montserrat",sans-serif;font-weight:600;color:var(--navy);font-size:22px;letter-spacing:4px;display:flex;align-items:center;gap:10px}
.brand i{width:12px;height:12px;background:var(--rose);display:block}
.nav{display:flex;gap:30px;font-size:11px;font-weight:600;letter-spacing:1px;color:var(--navy)}
.nav .active{color:var(--rose-deep)}

.hero{position:relative;height:480px;background:linear-gradient(90deg,var(--blush-light) 0%,var(--blush) 55%,#e9c6c6 100%)}
.hero-photo{position:absolute;right:0;top:0;width:560px;height:480px;background:radial-gradient(circle at 55% 45%,#d7b7b2 0%,#b9948f 35%,#7d6665 70%,#4a3f45 100%)}
.hero-copy{position:absolute;left:60px;top:40px;width:540px}
.hero h1{font-family:"Playfair Display",serif;font-weight:700;color:var(--navy);font-size:44px;line-height:1.08;letter-spacing:1px}
.hero ul{list-style:none;margin-top:26px;display:grid;gap:10px}
.hero li{display:flex;gap:10px;font-size:13px;color:var(--navy)}
.hero li::before{content:"";flex:0 0 8px;height:8px;margin-top:6px;background:var(--rose-deep);border-radius:50%}
.stats{position:absolute;left:60px;top:330px;display:flex;gap:30px}
.stat b{display:block;font-family:"Playfair Display",serif;font-size:56px;color:var(--navy);line-height:1}
.stat p{width:150px;font-size:10px;color:var(--muted);margin-top:6px;line-height:1.4}

.quality{text-align:center;padding-top:14px}
.quality h2{margin:0 auto;width:760px;background:var(--rose);color:var(--white);font-size:16px;letter-spacing:2px;font-weight:600;padding:10px 0}
.quality .sub{margin-top:12px;font-size:13px;color:var(--navy);font-weight:500}

.serum{display:flex;gap:40px;padding:26px 60px 0;height:250px}
.serum-photo{flex:0 0 520px;height:220px;background:linear-gradient(120deg,#f1e7e5,#cfc3c3 55%,#8e8791)}
.serum-text h3{font-size:15px;color:var(--navy);letter-spacing:1px;margin-bottom:14px}
.serum-text p{font-size:12px;color:var(--muted)}
.lead{padding:16px 60px 0;font-size:12px;color:var(--muted)}
.btn{display:inline-block;background:var(--navy);color:var(--white);font-size:11px;font-weight:600;letter-spacing:1.5px;padding:9px 22px}
.center{text-align:center}
.lead-btn{margin-top:22px}

.section-title{display:flex;align-items:center;gap:24px;padding:44px 60px 30px}
.section-title::before,.section-title::after{content:"";flex:1;height:1px;background:var(--rose)}
.section-title h2{font-size:26px;color:var(--navy);letter-spacing:3px}

.row{display:flex;height:250px;padding:0 60px}
.row .tile{flex:1;position:relative}
.photo-lash{background:linear-gradient(130deg,#e9dfde,#c4b5b8 50%,#6e6570)}
.photo-brow{background:linear-gradient(230deg,#f0e3e1,#cdb3b5 55%,#7c6b73)}
.tile .caption{position:absolute;left:30px;top:30px;color:var(--navy)}
.tile .caption h4{font-size:14px;letter-spacing:1px}
.tile .caption span{font-size:12px;color:var(--navy-soft)}
.tile .caption.right{left:auto;right:30px;text-align:right}
.box{padding:34px 40px;font-size:12px;line-height:1.7}
.box.navy{background:var(--navy);color:#e3e3ee}
.box.pink{background:var(--blush);color:var(--navy)}
.box.plain{background:var(--white);color:var(--muted)}
.row.short{height:210px}

.cards{display:flex;gap:30px;padding:30px 60px 0}
.card{flex:1;height:460px;display:flex;flex-direction:column}
.card-photo{height:200px;position:relative;background:linear-gradient(160deg,var(--blush-light),#dcc2c4)}
.card-photo h4{position:absolute;left:0;right:0;top:72px;text-align:center;font-size:14px;letter-spacing:1.5px;color:var(--navy);padding:0 30px}
.card-body{flex:1;background:var(--navy);color:#e3e3ee;padding:30px;font-size:12px;display:flex;flex-direction:column;justify-content:space-between}
.card-body .btn{align-self:center;background:var(--rose);font-size:10px;padding:7px 20px}

.footer{position:absolute;left:0;top:2384px;width:1200px;height:340px;background:var(--footer)}
.footer-grid{display:flex;gap:60px;padding:50px 60px 0}
.footer .brand{font-size:20px}
.footer-about p{font-size:11px;color:var(--muted);margin-top:12px;width:200px}
.footer h5{font-size:12px;letter-spacing:1.5px;color:var(--navy);margin-bottom:12px}
.footer ul{list-style:none;font-size:11px;color:var(--muted);display:grid;gap:4px}
.contact li{display:flex;gap:8px;align-items:center}
.contact svg{flex:0 0 12px}
.newsletter{margin-left:auto;width:300px;background:var(--rose);color:var(--white);padding:24px}
.newsletter h5{color:var(--white);font-family:"Playfair Display",serif;font-size:20px;letter-spacing:0}
.newsletter p{font-size:11px}
.newsletter .field{margin-top:14px;height:30px;background:var(--white)}
.newsletter .btn{margin-top:10px;font-size:10px;padding:7px 18px}
.footer-bottom{position:absolute;left:0;bottom:0;width:100%;height:44px;background:var(--navy)}
</style>
</head>
<body>

<div class="topbar">
  <div class="langs"><span></span><span></span></div>
  <span>info@lyravelbeauty.ch</span>
</div>

<header class="header">
  <div class="brand"><i></i>LYRAVEL</div>
  <nav class="nav">
    <a class="active" href="#">STARTSEITE</a>
    <a href="#">ÜBER UNS</a>
    <a href="#">KLINISCHE UNTERSUCHUNGEN</a>
    <a href="#">PRODUKTE</a>
    <a href="https://www.lyravelbeauty.shopvela.ch/">GESCHÄFT</a>
    <a href="#">KONTAKT</a>
  </nav>
</header>

<section class="hero">
  <div class="hero-photo" role="img" aria-label="Porträt einer Frau beim Auftragen des Wimpernserums"></div>
  <div class="hero-copy">
    <h1>THE PROMISE<br>OF A LONGER<br>LOOK</h1>
    <ul>
      <li>Innovative ingredients that guarantee your eyelashes becoming longer and thicker after just 15 days of regular usage</li>
      <li>It's safety has been attested by two independent clinical tests</li>
      <li>It's effectiveness has been attested in three independent application tests</li>
    </ul>
  </div>
  <div class="stats">
    <div class="stat"><b>100%</b><p>der Anwenderinnen bestätigen sichtbar längere Wimpern nach vier Wochen</p></div>
    <div class="stat"><b>97%</b><p>bemerkten dichtere und kräftigere Wimpern bereits nach zwei Wochen</p></div>
    <div class="stat"><b>98%</b><p>würden das Serum ihren Freundinnen empfehlen und erneut kaufen</p></div>
  </div>
</section>

<section class="quality">
  <h2>KOSMETIKARTIKEL VON HOHER QUALITÄT</h2>
  <p class="sub">Setzen Sie auf bewährte Produkte</p>
</section>

<section class="serum">
  <div class="serum-photo" role="img" aria-label="Nahaufnahme eines Auges mit langen Wimpern"></div>
  <div class="serum-text">
    <h3>SERUM FÜR IHRE WIMPERN</h3>
    <p>Wimpern, schöner Effekt, aber vielleicht keine Qualität? Das sind nur einige von den Eigenschaften, die ein gutes Wimpernserum auszeichnen sollten. Bei der Anwendung eines bestimmten Produktes finden wir grosse Erwartungen an dieses Produkt. Unser Serum für Wimpern soll sie verlängern, stärker machen und nähren. Richtig ist auch die Wirkung von dichten und schwarzen Wimpern.</p>
  </div>
</section>

<section class="lead">
  <p>Indem wir Produkte der Marke LYRAVEL BEAUTY verwenden, können wir sicher sein, dass die hervorragende Qualität auf speziell zusammengesetzten Inhaltsstoffen beruht. Die durch zwei unabhängige Labore bestätigte Sicherheit und Wirksamkeit macht das Serum zu einem verlässlichen Begleiter. Die ersten Effekte der Anwendung des Wimpernserums sind bereits nach wenigen Wochen sichtbar: die Wimpern werden länger, dichter und glänzender, ohne dass die natürliche Schönheit verloren geht.</p>
  <div class="center lead-btn"><a class="btn" href="https://www.lyravelbeauty.shopvela.ch/">VISIT OUR WEBSHOP</a></div>
</section>

<div class="section-title"><h2 class="serif">UNSER PRODUKTE</h2></div>

<section class="row">
  <div class="tile photo-lash" role="img" aria-label="Auge mit geschwungenen Wimpern">
    <div class="caption"><h4>LYRAVEL SERUM FÜR WIMPERN</h4><span>Wirkung</span></div>
  </div>
  <div class="tile box navy">Das Produkt hat sichtbare Wirkung. Erstens, aktive Inhaltsstoffe dringen in die Haarwurzeln ein und versorgen sie mit Nährstoffen. Zweitens werden die Wimpern kräftiger und brechen seltener ab. Die Wirkung ist dauerhaft, wenn das Serum regelmässig jeden Abend auf den oberen Lidrand aufgetragen wird.</div>
</section>

<section class="row">
  <div class="tile box pink">Ein Serum, das das Wachstum der Wimpern stimuliert, ist bei der Anwendung sehr einfach. Tragen Sie eine dünne Linie am Ansatz der oberen Wimpern auf, einmal täglich, am besten vor dem Schlafengehen. Die Haut sollte sauber und trocken sein. Nach vier Wochen zeigen sich die ersten Ergebnisse.</div>
  <div class="tile photo-brow" role="img" aria-label="Auftragen des Serums am Wimpernkranz">
    <div class="caption right"><h4>SERUM, DAS WACHSTUM<br>DER WIMPERN STIMULIERT</h4><span>Die Anwendungstipps</span></div>
  </div>
</section>

<section class="row short">
  <div class="tile box plain">Ein Vorteil ist ausserdem, dass das Produkt von Kontaktlinsenträgerinnen ohne Bedenken verwendet werden kann. Die Formel ist augenärztlich getestet und frei von Parfum.</div>
  <div class="tile box navy">Die Ergebnisse bleiben bei regelmässiger Pflege sichtbar erhalten. Wer die Anwendung beendet, sieht die Wimpern langsam wieder in ihren natürlichen Zustand zurückkehren.</div>
</section>

<section class="cards">
  <article class="card">
    <div class="card-photo" role="img" aria-label="Produktbild Wimpern- und Brauenconditioner"><h4>AURELLE EYELASH AND BROW CONDITIONER</h4></div>
    <div class="card-body"><p>Der kraftvolle Conditioner für Wimpern und Brauen stärkt jedes einzelne Haar und schützt vor dem Ausfallen.</p><a class="btn" href="https://www.lyravelbeauty.shopvela.ch/">SEE MORE</a></div>
  </article>
  <article class="card">
    <div class="card-photo" role="img" aria-label="Produktbild Volumen-Mascara"><h4>VELINA VOLUMIZING MASCARA</h4></div>
    <div class="card-body"><p>Die volumengebende Mascara trennt und verlängert die Wimpern, ohne zu verkleben, für einen ausdrucksstarken Blick.</p><a class="btn" href="https://www.lyravelbeauty.shopvela.ch/">SEE MORE</a></div>
  </article>
  <article class="card">
    <div class="card-photo" role="img" aria-label="Produktbild Haarconditioner"><h4>CORISA MULTITASKING HAIR CONDITIONER</h4></div>
    <div class="card-body"><p>Der Multitasking-Conditioner pflegt das Haar von der Wurzel bis in die Spitzen und verleiht neuen Glanz.</p><a class="btn" href="https://www.lyravelbeauty.shopvela.ch/">SEE MORE</a></div>
  </article>
</section>

<footer class="footer">
  <div class="footer-grid">
    <div class="footer-about">
      <div class="brand"><i></i>LYRAVEL</div>
      <p>Hochwertige Pflege für Wimpern und Haar.</p>
    </div>
    <div>
      <h5>QUICK LINKS</h5>
      <ul>
        <li>Startseite</li><li>Über Uns</li><li>Klinische Untersuchungen</li><li>Produkte</li><li>Geschäft</li><li>Kontakt</li>
      </ul>
    </div>
    <div>
      <h5>KONTAKT</h5>
      <ul class="contact">
        <li><svg width="12" height="12" viewBox="0 0 12 12"><path d="M6 1a3.5 3.5 0 0 0-3.5 3.5C2.5 7.5 6 11 6 11s3.5-3.5 3.5-6.5A3.5 3.5 0 0 0 6 1z" fill="var(--rose-deep)"/></svg>Musterstrasse 12, 8000 Zürich</li>
        <li><svg width="12" height="12" viewBox="0 0 12 12"><rect x="1" y="2.5" width="10" height="7" fill="none" stroke="var(--rose-deep)"/><path d="M1 2.5l5 4 5-4" fill="none" stroke="var(--rose-deep)"/></svg>info@lyravelbeauty.ch</li>
        <li><svg width="12" height="12" viewBox="0 0 12 12"><path d="M3 1l2 2.5-1 1.5a6 6 0 0 0 3 3l1.5-1L11 9l-1.5 2A9 9 0 0 1 1 2.5z" fill="var(--rose-deep)"/></svg>+41 44 000 00 00</li>
        <li>www.lyravelbeauty.ch</li>
      </ul>
    </div>
    <div class="newsletter">
      <h5>Newsletter</h5>
      <p>Erhalten Sie Neuigkeiten und exklusive Angebote.</p>
      <div class="field"></div>
      <a class="btn" href="#">ABONNIEREN</a>
    </div>
  </div>
  <div class="footer-bottom"></div>
</footer>

</body>
</html>
```